Civil engineering company | Billboard

We need a billboard design for Velmora- civil engineering company. We want big logo in the center of billboard and web site (www.velmora.hr) below the logo. Also, we want an subtle abstract pattern in the background. Dimensions of the billboard are: width :10 m, height: 2m. Design must be celan and modern.
Industry/Entity Type
Civil engineering
Font styles to use
Sans Serif
Colors
F0912C
F2A743
F7CA91
FBE8D2
FDF5EE
Requirements
Must have
- Logo and new unique pattern design for Velmroa company
Should not have
- pictures of construction machinery and tools

```html
<!DOCTYPE html>
<html lang="hr">
<head>
<meta charset="utf-8">
<title>Velmora – billboard</title>
<link rel="stylesheet" href="https://fonts.googleapis.com/css2?family=Montserrat:wght@500;600;800&family=Open+Sans:wght@400;700&display=swap">
<style>
  :root {
    --orange: #e89236;
    --orange-soft: #f7ca91;
    --orange-pale: #fbe8d2;
    --cream: #fdf5ee;
    --grey: #666666;
    --grey-line: #7a7a7a;
    --white: #ffffff;
    --page: #eceef1;
  }
  html, body {
    margin: 0;
    padding: 0;
    width: 720px;
    height: 1200px;
    overflow: hidden;
    background: var(--page);
  }
  .canvas {
    position: relative;
    width: 720px;
    height: 1200px;
  }
  .billboard {
    position: absolute;
    left: 60px;
    width: 600px;
    height: 116px;
    display: block;
    box-shadow: 0 4px 14px rgba(0,0,0,.12);
  }
  .billboard--angled { top: 218px; }
  .billboard--banded { top: 775px; }
  .board-bg { fill: var(--white); stroke: var(--grey-line); stroke-width: 1; }
  .mark-square { fill: none; stroke: var(--grey); stroke-width: 2; }
  .corner-grey { fill: var(--grey); }
  .corner-orange { fill: var(--orange); }
  .band-grey { fill: var(--grey); }
  .base-line { fill: var(--orange); }
  .wordmark {
    font-family: "Montserrat", sans-serif;
    font-weight: 500;
    fill: var(--orange);
    letter-spacing: 6px;
  }
  .web--bold {
    font-family: "Montserrat", sans-serif;
    font-weight: 800;
    fill: var(--grey);
    letter-spacing: 3px;
  }
  .tagline {
    font-family: "Open Sans", sans-serif;
    font-weight: 400;
    fill: var(--grey);
  }
  .web--light {
    font-family: "Open Sans", sans-serif;
    font-weight: 700;
    fill: var(--white);
  }
</style>
</head>
<body>
<div class="canvas">

  <svg class="billboard billboard--angled" viewBox="0 0 600 116" xmlns="http://www.w3.org/2000/svg">
    <rect class="board-bg" x="0.5" y="0.5" width="599" height="115"/>
    <polygon class="corner-grey" points="531,1 599,1 599,64"/>
    <polygon class="corner-orange" points="480,115 565,32 599,64 599,115"/>
    <rect class="mark-square" x="22" y="21" width="80" height="76"/>
    <text class="wordmark" x="114" y="60" font-size="52">VELMORA</text>
    <text class="web--bold" x="150" y="92" font-size="21">www.velmora.hr</text>
  </svg>

  <svg class="billboard billboard--banded" viewBox="0 0 600 116" xmlns="http://www.w3.org/2000/svg">
    <defs>
      <linearGradient id="stripFill" x1="0" y1="0" x2="0" y2="1">
        <stop offset="0" stop-color="#fdf5ee"/>
        <stop offset="0.5" stop-color="#fbe8d2"/>
        <stop offset="1" stop-color="#f7ca91"/>
      </linearGradient>
    </defs>
    <rect class="board-bg" x="0.5" y="0.5" width="599" height="115"/>
    <rect class="mark-square" x="39" y="22" width="62" height="60"/>
    <text class="wordmark" x="116" y="64" font-size="52">VELMORA</text>
    <text class="tagline" x="117" y="84" font-size="11.5">IZVOĐENJE I VOĐENJE GRAĐEVINSKIH RADOVA</text>
    <rect x="1" y="88" width="380" height="21" fill="url(#stripFill)" role="img" aria-label="Subtle abstract pattern strip in pale orange tones"/>
    <rect class="base-line" x="1" y="109" width="380" height="4"/>
    <polygon class="band-grey" points="378,88 599,88 599,115 362,115"/>
    <text class="web--light" x="571" y="109" font-size="17" text-anchor="end">www.velmora.hr</text>
  </svg>

</div>
</body>
</html>
```